Fall Event Advertisement for Hearthside Magazine

I will be taking out an ad in Hearthside Magazine to promote the fall events in our community. The audience is middle to upper class, primarily women, looking for fun activities and weekend getaways. The add should include our logo, contact info, a heading, like Discover Columbus County Fall Festivals & Events or something like that. I appreciate the creativity with the copy.

I have uploaded some photos. They all do not need to be used.

Contact info: Brightwater Chamber of Commerce & Tourism
417 N Alder Ave
Whiteville, NC 28519
(910) 555-0187
For a full listing of year-round events, check out our calendar here, www.thebrightwaterchamber.example

Ad size: 8.25 inches x 10.875 inches

```html
<!DOCTYPE html>
<html lang="en">
<head>
<meta charset="utf-8">
<title>Discover County Fall Festivals &amp; Events</title>
<link rel="stylesheet" href="https://fonts.googleapis.com/css2?family=Outfit:wght@300;400;600;700;800;900&display=swap">
<style>
  :root {
    --orange: #f5871f;
    --blue: #2b3990;
    --detail: #3f4c94;
    --shadow: #b9bcc6;
    --paper: #f1f2f6;
  }
  * { box-sizing: border-box; margin: 0; padding: 0; }
  html, body { width: 910px; height: 1200px; overflow: hidden; }
  body { font-family: "Outfit", sans-serif; background: var(--paper); }
  .ad {
    position: relative; width: 910px; height: 1200px; overflow: hidden;
    background: linear-gradient(160deg, #f4f1ec 0%, #eceef4 40%, #e6e9f1 70%, #eeeef2 100%);
  }
  .ad-backdrop {
    position: absolute; inset: 0;
    background: radial-gradient(ellipse at 30% 60%, rgba(200,190,200,.35), transparent 60%),
                radial-gradient(ellipse at 80% 70%, rgba(170,180,210,.35), transparent 60%);
  }
  .autumn-garland {
    position: absolute; left: 140px; top: 0; width: 636px; height: 215px;
    background: radial-gradient(closest-side, rgba(232,134,42,.95) 0%, rgba(242,164,68,.85) 40%, rgba(246,204,126,.5) 70%, rgba(246,220,170,0) 100%);
  }
  .headline {
    position: absolute; left: 0; right: 0; top: 196px; text-align: center;
    font-weight: 800; font-size: 108px; line-height: 1; letter-spacing: -1px;
    color: var(--orange); text-shadow: 4px 4px 0 var(--shadow);
  }
  .banner { position: absolute; left: 85px; top: 309px; width: 740px; height: 54px; }
  .banner svg { position: absolute; inset: 0; }
  .banner-text {
    position: absolute; left: 0; right: 0; top: 0; line-height: 54px; text-align: center;
    font-weight: 700; font-size: 37px; color: var(--orange); letter-spacing: -.3px;
  }
  .divider { position: absolute; left: 319px; top: 386px; width: 3px; height: 678px; background: var(--blue); }
  .date { position: absolute; left: 96px; width: 220px; text-align: center; }
  .date-month { display: block; font-weight: 800; font-size: 28px; line-height: 28px; color: var(--orange); }
  .date-days { display: block; font-weight: 800; font-size: 49px; line-height: 52px; margin-top: 4px; color: var(--blue); }
  .event { position: absolute; left: 357px; width: 530px; }
  .event-title { font-weight: 600; font-size: 27px; line-height: 30px; color: var(--orange); }
  .event-place { font-weight: 700; font-style: italic; font-size: 19.5px; line-height: 26px; color: var(--blue); }
  .event-details { font-weight: 300; font-size: 20px; line-height: 26px; color: var(--detail); }
  .brand { position: absolute; left: 120px; top: 1079px; width: 200px; text-align: center; }
  .brand-dot { display: block; width: 52px; height: 52px; margin: 0 auto 8px; border-radius: 50%; background: var(--blue); }
  .brand-name { font-weight: 700; font-size: 13.5px; line-height: 16px; color: var(--blue); text-transform: uppercase; }
  .contact { position: absolute; left: 357px; top: 1093px; font-style: normal; font-size: 14.5px; line-height: 19.5px; color: var(--blue); }
  .contact-org, .contact-address { font-weight: 700; font-style: normal; }
  .contact-note { font-style: italic; font-weight: 600; }
  .contact-web { font-style: italic; font-weight: 800; color: var(--orange); }
</style>
</head>
<body>
<main class="ad">
  <div class="ad-backdrop" role="img" aria-label="Faded collage of fall festival photos: parades, flags, dancers and food stalls"></div>
  <div class="autumn-garland" role="img" aria-label="Illustrated garland of autumn leaves, red berries and apples"></div>

  <h1 class="headline">DISCOVER</h1>
  <div class="banner">
    <svg width="740" height="54" viewBox="0 0 740 54"><polygon points="28,0 740,0 712,54 0,54" fill="var(--blue)"/></svg>
    <h2 class="banner-text">COUNTY FALL FESTIVALS &amp; EVENTS</h2>
  </div>

  <div class="divider"></div>

  <div class="date" style="top:386px"><span class="date-month">SEPTEMBER</span><span class="date-days">02-04</span></div>
  <div class="event" style="top:384px">
    <p class="event-title">Lakeside Challenge</p>
    <p class="event-place">Lake Marlow, NC</p>
    <p class="event-details">Run • Bike • Swim • Paddle</p>
  </div>

  <div class="date" style="top:485px"><span class="date-month">SEPTEMBER</span><span class="date-days">24</span></div>
  <div class="event" style="top:484px">
    <p class="event-title">Harvest Stew Festival</p>
    <p class="event-place">Brunswick, NC</p>
    <p class="event-details">Parade • Family Fun • Good Eats</p>
  </div>

  <div class="date" style="top:588px"><span class="date-month">OCTOBER</span><span class="date-days">11-26</span></div>
  <div class="event" style="top:588px">
    <p class="event-title">Brightwater County Agricultural Fair</p>
    <p class="event-place">Whiteville, NC</p>
    <p class="event-details">Carnival Rides • Tractor Pull • Demolition<br>Derby • Live Entertainment</p>
  </div>

  <div class="date" style="top:721px"><span class="date-month">OCTOBER</span><span class="date-days">15-16</span></div>
  <div class="event" style="top:721px">
    <p class="event-title">Autumn Heritage Gathering</p>
    <p class="event-place">Buckhead, NC</p>
    <p class="event-details">Traditional Foods • History • American Indian<br>Dance &amp; Drumming Competition</p>
  </div>

  <div class="date" style="top:846px"><span class="date-month">OCTOBER</span><span class="date-days">22</span></div>
  <div class="event" style="top:845px">
    <p class="event-title">Sweet Potato Festival</p>
    <p class="event-place" style="margin-top:8px">Tabor City, NC</p>
    <p class="event-details">Arts &amp; Crafts • Parade • Food • Entertainment</p>
  </div>

  <div class="date" style="top:950px"><span class="date-month">NOVEMBER</span><span class="date-days">04-05</span></div>
  <div class="event" style="top:950px">
    <p class="event-title">Pecan Harvest Days</p>
    <p class="event-place" style="margin-top:4px">Whiteville, NC</p>
    <p class="event-details">Car Show • Entertainment • Burger Brawl<br>• Beer Garden</p>
  </div>

  <div class="brand">
    <span class="brand-dot"></span>
    <p class="brand-name">Brightwater Chamber<br>of Commerce &amp; Tourism</p>
  </div>

  <address class="contact">
    <p class="contact-org">Brightwater Chamber of Commerce &amp; Tourism</p>
    <p class="contact-address">417 N Alder Ave Whiteville, NC 28519 | (910) 555-0187</p>
    <p class="contact-note">For a full listing of year-round events, check out our calendar here,</p>
    <p class="contact-web">www.thebrightwaterchamber.example</p>
  </address>
</main>
</body>
</html>
```